Postcard Design

My company name is Perch Skyward. We offer FAA approved drone photography and videography for real estate marketing. Our target demographic customer base is Realtors, Real Estate Brokerages (their Brokers in Charge "BIC's and owners), Builders and Developers. There are currently only two FAA approved drone operators in the greater Raleigh "Lattice" area. Our website is www.PerchSkyward-demo.com. All current packages and pricing are featured there. Our prices are extremely affordable by design to make drone marketing available to all types of real estate rather than just the luxury markets. I have a Perch Lattice logo for our real estate business but I'd like to modify it a bit to replace "Homes Colective" with "Aerial" and have an image of a ZQR Osprey V underneath Perch (black with the same effect as the word "Lattice". I'll provide examples of my photography as well as the logo I'd like modified. I'd like this post card to be eye catching and include a 25% off promotion off all our packages through January, 2016. The postcard can be two sided. Our motto is "Let Perch Skyward take your real estate marketing to new heights". I prefer a clean contemporary feel rather than the cartoonish cluttered look.

Industry/Entity Type

Real Estate

```html
<!DOCTYPE html>
<html lang="en">
<head>
<meta charset="utf-8">
<title>Perch Skyward – Postcard</title>
<link href="https://fonts.googleapis.com/css2?family=Roboto+Condensed:ital,wght@0,400;0,700;1,700&display=swap" rel="stylesheet">
<style>
  :root{
    --paper:#eceef1;
    --white:#ffffff;
    --navy:#1d6887;
    --steel:#a6bcc5;
    --orange:#f2925a;
    --orange-deep:#ef8a4f;
    --ink:#222222;
    --muted:#555a5e;
    --card-top:#eef1f4;
    --card-base:#e8e7df;
  }
  *{box-sizing:border-box;margin:0;padding:0}
  html,body{width:1200px;height:775px;overflow:hidden;background:var(--paper)}
  body{font-family:"Roboto Condensed",Arial,sans-serif}
  .postcard{position:relative;width:1200px;height:775px;background:var(--paper);overflow:hidden}

  .brand-panel{position:absolute;left:0;top:0;width:326px;height:193px;background:var(--white);
    display:flex;align-items:center;justify-content:center;gap:12px}
  .brand-dot{width:18px;height:18px;background:var(--ink)}
  .brand-name{font-weight:700;font-size:42px;color:var(--ink);letter-spacing:-0.5px}

  .promo-tag{position:absolute;left:427px;top:34px;width:712px;height:146px;transform:rotate(2deg);transform-origin:left center}
  .promo-tag svg{position:absolute;inset:0}
  .promo-text{position:absolute;left:110px;top:18px;display:flex;align-items:center;gap:20px}
  .promo-amount{font-weight:700;font-size:84px;color:var(--white);letter-spacing:-2px;line-height:1}
  .promo-amount small{font-size:60px}
  .promo-detail{color:var(--navy);font-weight:700;line-height:1}
  .promo-detail .line-1{font-size:44px;display:block}
  .promo-detail .line-2{font-size:34px;display:block;margin-top:2px}

  .pricing-band{position:absolute;left:0;top:193px;width:1200px;height:134px;background:var(--navy)}
  .package{position:absolute;top:19px;width:252px}
  .package-name{height:41px;background:var(--card-top);color:var(--navy);font-weight:700;font-size:28px;
    text-align:center;line-height:43px}
  .package-price{margin-top:4px;height:51px;background:var(--card-base);display:flex;align-items:center;
    justify-content:space-between;padding:0 8px 0 10px}
  .price-old{font-weight:700;font-size:34px;color:var(--muted);position:relative}
  .price-old::after{content:"";position:absolute;left:-4px;right:-4px;top:50%;height:5px;background:var(--white);opacity:.85}
  .price-old sup,.price-new sup{font-size:.55em;vertical-align:-0.1em}
  .price-new{font-weight:700;font-style:italic;font-size:46px;color:var(--orange-deep);letter-spacing:-1px}
  .price-new .cents{font-size:26px}
  .price-new sup{font-size:26px}

  .gallery-band{position:absolute;left:0;top:362px;width:1200px;height:288px;background:var(--steel)}
  .photo{position:absolute;top:17px;height:253px}
  .photo-estate{left:38px;width:336px;background:linear-gradient(160deg,#3f6b2c 0%,#7fb446 45%,#9cc657 100%)}
  .photo-home{left:432px;width:339px;background:linear-gradient(180deg,#9fc3e8 0%,#4c6e3a 45%,#5f8f3a 75%,#cfc9bb 100%)}
  .photo-cabin{left:831px;width:336px;background:linear-gradient(180deg,#2f4a23 0%,#7fa346 40%,#a4813a 60%,#8fae4d 100%)}

  .motto-band{position:absolute;left:0;top:686px;width:1200px;height:89px;background:var(--navy);
    display:flex;align-items:center;justify-content:center}
  .motto{font-weight:700;font-size:41px;color:var(--orange);letter-spacing:0.2px;white-space:nowrap}
  .motto .name{color:var(--white)}
</style>
</head>
<body>
<div class="postcard">

  <header class="brand-panel">
    <span class="brand-dot"></span>
    <span class="brand-name">Perch Skyward</span>
  </header>

  <div class="promo-tag">
    <svg width="712" height="146" viewBox="0 0 712 146">
      <polygon points="70,0 712,0 712,146 70,146 0,73" fill="var(--orange)"/>
      <circle cx="62" cy="73" r="11" fill="var(--paper)"/>
    </svg>
    <div class="promo-text">
      <span class="promo-amount">25<small>%</small> off</span>
      <span class="promo-detail">
        <span class="line-1">all our packages</span>
        <span class="line-2">through January, 2016</span>
      </span>
    </div>
  </div>

  <section class="pricing-band">
    <div class="package" style="left:38px">
      <div class="package-name">STARTER</div>
      <div class="package-price"><span class="price-old"><sup>$</sup>99</span><span class="price-new"><sup>$</sup>74<span class="cents">,25</span></span></div>
    </div>
    <div class="package" style="left:329px">
      <div class="package-name">EXPERT</div>
      <div class="package-price"><span class="price-old"><sup>$</sup>149</span><span class="price-new"><sup>$</sup>111<span class="cents">,75</span></span></div>
    </div>
    <div class="package" style="left:619px">
      <div class="package-name">TOP PRODUCER</div>
      <div class="package-price"><span class="price-old"><sup>$</sup>399</span><span class="price-new"><sup>$</sup>299<span class="cents">,25</span></span></div>
    </div>
    <div class="package" style="left:911px">
      <div class="package-name">FREQUENT FLYER</div>
      <div class="package-price"><span class="price-old"><sup>$</sup>600</span><span class="price-new"><sup>$</sup>450<span class="cents">,00</span></span></div>
    </div>
  </section>

  <section class="gallery-band">
    <div class="photo photo-estate" role="img" aria-label="Aerial photo of a country home with a winding driveway across green lawns"></div>
    <div class="photo photo-home" role="img" aria-label="Aerial photo of a suburban house front with driveway framed by trees"></div>
    <div class="photo photo-cabin" role="img" aria-label="Aerial photo of a log cabin home with a deck on a sunny lawn"></div>
  </section>

  <footer class="motto-band">
    <p class="motto">Let <span class="name">Perch Skyward</span> take your real estate marketing to new heights!</p>
  </footer>

</div>
</body>
</html>
```